Business Card Design for Marketing Firm

Looking for business card design for higher end marketing firm. Clean but impressionable/trendy. We are a marketing firm that represents manufacturers in the foodservice equipment and supply industry. Our customers are end users such has hotels, restaurants, country clubs, convention centers and casinos as well as distributors of restaurants supplies and equipment, and manufacturers of foodservice equipment and supplies.
Target Market(s)
Hotels, Restaurants, Supply & Equipment Distributors, Foodservice Manufacturers
Industry/Entity Type
Foodservice/Hospitality
Contact Information for Business Card
Name, Title, Contact Number, Email, Website, Social Media, Address
Requirements
Must have
- Clean & Simple but Serious and Impressionable

```html
<!DOCTYPE html>
<html lang="en">
<head>
<meta charset="utf-8">
<title>Meridian Hospitality Reps — Business Card</title>
<link rel="stylesheet" href="https://fonts.googleapis.com/css2?family=Cinzel:wght@400&family=Noto+Serif:wght@700&family=Arimo:wght@400&display=swap">
<style>
  :root {
    --backdrop: #1c1c1d;
    --paper: #f3f3f3;
    --navy: #262c6b;
    --ink: #3a3a3a;
    --white: #ffffff;
  }
  * { margin: 0; padding: 0; box-sizing: border-box; }
  html, body { width: 1200px; height: 1059px; overflow: hidden; background: var(--backdrop); }
  .canvas { position: relative; width: 1200px; height: 1059px; }

  .card { position: absolute; width: 690px; height: 392px; border-radius: 18px; overflow: hidden; }
  .card--front { left: 256px; top: 89px; background: var(--paper); }
  .card--back { left: 254px; top: 547px; background: var(--navy); }

  .brand { position: absolute; text-align: center; font-family: "Cinzel", serif; font-weight: 400; }
  .brand__mark { display: block; margin: 0 auto; border-radius: 50%; }
  .brand__name { display: block; white-space: nowrap; letter-spacing: 0.5px; }
  .brand__sub { display: block; text-align: right; }

  .card--front .brand { left: 42px; top: 118px; width: 280px; color: var(--navy); }
  .card--front .brand__mark { width: 44px; height: 44px; background: var(--navy); margin-bottom: 20px; }
  .card--front .brand__name { font-size: 19px; line-height: 24px; }
  .card--front .brand__sub { font-size: 15px; line-height: 18px; }

  .divider { position: absolute; left: 344px; top: 100px; width: 1.5px; height: 191px; background: var(--navy); }

  .contact { position: absolute; left: 374px; top: 90px; font-family: "Arimo", sans-serif; color: var(--ink); }
  .contact__name { font-family: "Noto Serif", serif; font-weight: 700; font-size: 25px; line-height: 30px; color: var(--navy); letter-spacing: 0.3px; }
  .contact__title { font-size: 16px; line-height: 20px; }
  .contact__address { margin-top: 12px; font-size: 16px; line-height: 20px; }
  .contact__list { list-style: none; margin-top: 11px; }
  .contact__item { display: flex; align-items: center; font-size: 16px; line-height: 23.5px; }
  .contact__icon { width: 12px; height: 12px; margin-right: 7px; flex: none; }
  .contact__dot { width: 11px; height: 11px; border-radius: 50%; background: var(--navy); margin-right: 8px; flex: none; }

  .card--back .brand { left: 95px; top: 140px; width: 500px; color: var(--white); }
  .card--back .brand__mark { width: 64px; height: 64px; background: var(--white); margin-bottom: 30px; }
  .card--back .brand__name { font-size: 31px; line-height: 38px; }
  .card--back .brand__sub { font-size: 24px; line-height: 28px; }
</style>
</head>
<body>
<main class="canvas">
  <section class="card card--front">
    <div class="brand">
      <span class="brand__mark"></span>
      <span class="brand__name">MERIDIAN HOSPITALITY</span>
      <span class="brand__sub">REPS</span>
    </div>
    <div class="divider"></div>
    <div class="contact">
      <h1 class="contact__name">DANIEL WHITAKER</h1>
      <p class="contact__title">CEO/Founder</p>
      <p class="contact__address">48 Harbor Lane, Suite 210<br>Lakeview, ON 52318</p>
      <ul class="contact__list">
        <li class="contact__item">
          <svg class="contact__icon" viewBox="0 0 12 12" aria-hidden="true"><path fill="#262c6b" d="M1 4.5C1 2.5 3.5 2 6 2s5 .5 5 2.5v1H8.5V4.3H3.5v1.2H1zM2.5 6.5h7l1 4h-9z"/></svg>
          555-014-2290
        </li>
        <li class="contact__item">
          <svg class="contact__icon" viewBox="0 0 12 12" aria-hidden="true"><path fill="#262c6b" d="M1 3h10v7H1z"/><path fill="none" stroke="#f3f3f3" stroke-width="1" d="M1.5 3.5 6 7l4.5-3.5"/></svg>
          hello@meridianhospreps.com
        </li>
        <li class="contact__item">
          <svg class="contact__icon" viewBox="0 0 12 12" aria-hidden="true"><circle cx="6" cy="6" r="5" fill="#262c6b"/><path fill="none" stroke="#f3f3f3" stroke-width="0.8" d="M1 6h10M6 1c-2 2-2 8 0 10M6 1c2 2 2 8 0 10"/></svg>
          www.meridianhospreps.com
        </li>
        <li class="contact__item">
          <span class="contact__dot"></span>
          @meridianhospreps
        </li>
      </ul>
    </div>
  </section>

  <section class="card card--back">
    <div class="brand">
      <span class="brand__mark"></span>
      <span class="brand__name">MERIDIAN HOSPITALITY</span>
      <span class="brand__sub">REPS</span>
    </div>
  </section>
</main>
</body>
</html>
```